Presentation Folder Design for Photographer

Professional photographer requires a presentation folder for marketing.
I specialise in architecture, corporate & commercial photography. The folder will be used to promote my architectural photography services to real estate, accomodation & architect clients.

I'm looking for a modern clean design that complements my logo with complimentary text & colours. I want to use some images in the design, probably a mix of images not just architectural. I need a print ready design in PDF as well as a PSD file that I can possibly edit / update images later on.

The folder will be a double sided design with no need for pockets included in the design. Overall dimensions are 430mm ( folded down the centre ) x 315mm with a 5mm trim & bleed.

The layout would be as follows :

Front cover - Logo + maybe some images or some other design work.

Inside front cover - Some text about my services.

ARCHITECTURE
Commercial Residential Real Estate Drone Floorpans Accommodation

CORPORATE
Studio Headshots Environmental Portraits Staff Photography

COMMERCIAL
Product Advertising Fashion Event Stock

Inside back cover - no text as a seperate price list will sit here.

Outside back cover - I was thinking of having a collage of images worked into
the design but open to the designers input as well.
I also have another logo with phone number & web address
I would like on the back cover - Will be included in the files
provided.

I have a black background & white background version of my logo I will include both for the design work. I'm trying to get away from an all black design so if using the black logo I don't want a completely black page design, just becomes to heavy.

I'm redoing my website soon so please base the folder design around my logo text & colours not my current website as it's very outdated.

Logo brand guide is as follows

Main Font Font: Reislust
Main Font Color: #fff
Slogan Font Font: Ubuntu Bold
Monogram Font Font: Venti Medium
Container Color: #fff

Please respect the copyright on the images provided and delete all content once the design has been completed.
Thanks.

Need extra days to review

```html
<!DOCTYPE html>
<html lang="en">
<head>
<meta charset="UTF-8">
<title>Turning Light — Presentation Folder Front Cover</title>
<link rel="stylesheet" href="https://fonts.googleapis.com/css2?family=Josefin+Sans:wght@300;400&display=swap">
<style>
  :root {
    --backdrop: #e4e4e4;
    --paper: #f7f7f7;
    --ink: #2b2b2b;
    --gold-light: #f3e4a0;
    --gold-mid: #d9b960;
    --gold-deep: #a97c2c;
  }
  * { box-sizing: border-box; margin: 0; padding: 0; }
  html, body {
    width: 1200px;
    height: 900px;
    overflow: hidden;
    background: var(--backdrop);
    font-family: "Josefin Sans", sans-serif;
  }
  .cover {
    position: absolute;
    left: 306px;
    top: 20px;
    width: 588px;
    height: 860px;
    background: var(--paper);
    box-shadow: 0 2px 10px rgba(0,0,0,0.12);
  }
  .brand {
    position: absolute;
    top: 120px;
    left: 0;
    width: 100%;
    display: flex;
    justify-content: center;
    align-items: center;
    gap: 14px;
  }
  .brand-square {
    width: 34px;
    height: 34px;
    border: 3px solid var(--gold-mid);
  }
  .brand-name {
    font-weight: 300;
    font-size: 24px;
    letter-spacing: 3px;
    color: var(--ink);
    text-transform: uppercase;
  }
  .gold-band {
    position: absolute;
    background: linear-gradient(180deg, var(--gold-light) 0%, var(--gold-mid) 55%, var(--gold-deep) 100%);
  }
  .gold-band--left { left: 24px; width: 44px; top: 330px; height: 410px; }
  .gold-band--right { right: 24px; width: 44px; top: 190px; height: 410px; }
  .gallery {
    position: absolute;
    top: 240px;
    left: 68px;
    width: 452px;
    height: 430px;
    display: flex;
    gap: 16px;
  }
  .gallery-photo { flex: 1; height: 100%; }
  .gallery-photo--interior {
    background: linear-gradient(180deg, #e9ddd4 0%, #d8c6b8 35%, #c6a98c 55%, #f1efec 75%, #c9a98a 100%);
  }
  .gallery-photo--fashion {
    background: linear-gradient(180deg, #8c8f95 0%, #a08a6c 18%, #7c6a52 40%, #2a2a2a 60%, #4a4a4a 85%, #3a3a3a 100%);
  }
  .gallery-photo--residence {
    background: linear-gradient(180deg, #6c6f9a 0%, #a85a3c 25%, #b3573a 42%, #5b8a3c 58%, #6f5aa8 72%, #4f7f36 88%, #8a4a3a 100%);
  }
  .photographer {
    position: absolute;
    top: 742px;
    left: 0;
    width: 100%;
    text-align: center;
    font-weight: 400;
    font-size: 15px;
    letter-spacing: 3.5px;
    color: var(--ink);
    text-transform: uppercase;
  }
</style>
</head>
<body>
  <main class="cover">
    <div class="brand">
      <span class="brand-square"></span>
      <span class="brand-name">Turning Light</span>
    </div>
    <div class="gold-band gold-band--left"></div>
    <div class="gold-band gold-band--right"></div>
    <section class="gallery">
      <div class="gallery-photo gallery-photo--interior" role="img" aria-label="Photo of a bright bedroom with a chandelier and a wall of framed pictures above the bed"></div>
      <div class="gallery-photo gallery-photo--fashion" role="img" aria-label="Fashion photo of a model in a striped outfit holding black balloons in a stone doorway"></div>
      <div class="gallery-photo gallery-photo--residence" role="img" aria-label="Photo of a red brick house at dusk behind a flowering garden with a birdbath"></div>
    </section>
    <p class="photographer">Photographer Marcus Hale</p>
  </main>
</body>
</html>
```